Direct Mail Marketing Postcard Template Design

Mine is a residential real estate marketing service for "Fixer Upper" properties in Central Indiana. My company owns the properties being promoted on a proprietary/branded web site (also being developed by Harbor Press) and by Direct Mail . The properties for sale are not traditional real estate "listings".

I expect the post card and the web site to establish and promote the "new" brand for Blue Canyon Holdings, Inc.

The post card will be mailed to specific niche markets; primarily "Hands On" real estate investors, Rehabbers, Landlords, and First Time Home Buyers. The cards will routinely be mailed to investors and to residents in the area surrounding a property for sale to generate home buyer phone call inquiry, word of mouth referral, and to drive traffic to the (Harbor Press) web site.

The objective is to develop a post card template with clear and consistent brand imaging, but also with specific blank areas to be populated with multiple photos of respective properties which are to be uploaded with price and descriptive text - to be changed out with each new property being promoted for sale.

Blue Canyon Holdings, Inc. is an online and direct mail marketing service promoting available home buyer opportunities. The objective with each post card mailing is to capture lead contact information, and to promote the Blue Canyon Holdings brand. It is not important to promote any individual personality or person involved with Blue Canyon. Prospective buyer responses from the post card will be directed either to the dedicated web site, and/or to a dedicated customer service phone number. Both the URL and the dedicated phone # are to be highlighted on the post card.

In addition to specific properties for sale (photos and brief text on the front of card), an important function of the post card will be to promote various home buyer services (illustrated on the back of the card). Those various illustrated services are provided by an affiliated team of experienced professionals. The services are enumerated in the pencil concept draft attached with this application. Specifically those services are: Home Buyer Financing, Renovation Design Services, Project Cost Estimates, Rental Property Management, Professional CPA Consultation. Many of those services may be provided free of charge for qualified buyers.

Project Deadline Extended
Reason: I realize that the initial 3 day deadline is not realistic.

Target Market(s)

Real Estate Investors, Rehabbers, Landlords and First Time Home Buyers ...normally male, age 25-50 yr old.

Industry/Entity Type

Residential

Requirements
Must have
• 1. Ability to use basic template style for multiple property photo and text files.
2. A clear call to action and reference to dedicated web site URL and dedicated phone #.
3. Logo/branding to be consistent with web site and other promotional materials. i.e., business card, stationary, other template Blue Canyon post cards targeted to other niche markets.
Nice to have
• "Equity gain - opportunity - renovation" theme/background.

Clear distinct colors and photo images.

Trustworthy, reliable, professional look.
Should not have
• Casual/informal appearance.

Cluttered/overly detailed appearance.

```html
<!DOCTYPE html>
<html lang="en">
<head>
<meta charset="utf-8">
<title>Opportunity Sale Postcard</title>
<link rel="stylesheet" href="https://fonts.googleapis.com/css2?family=Roboto:ital,wght@0,300;0,400;0,500;0,700;1,400&family=Roboto+Condensed:wght@700&display=swap">
<style>
  :root {
    --page-bg: #ffffff;
    --cyan: #29b8e6;
    --panel-top: #3a3a3a;
    --panel-mid: #5e5e5e;
    --panel-black: #050505;
    --column-bg: #f3f5f7;
    --band: rgba(45, 45, 45, 0.74);
    --white: #ffffff;
    --caption: #222222;
    --lorem: #f0f0f0;
    --emblem: #1c1c1c;
  }
  * { box-sizing: border-box; margin: 0; padding: 0; }
  html, body { width: 1200px; height: 900px; overflow: hidden; background: var(--page-bg); }
  body { font-family: "Roboto", Arial, sans-serif; position: relative; }

  .postcard {
    position: absolute; top: 240px; width: 540px; height: 420px;
    background: var(--white); overflow: hidden;
    box-shadow: 0 2px 8px rgba(0,0,0,0.25);
  }
  .postcard--front { left: 40px; }
  .postcard--back { left: 620px; }

  /* Front */
  .hero-photo {
    position: absolute; left: 0; top: 0; width: 350px; height: 420px;
    background:
      radial-gradient(ellipse 60% 30% at 45% 38%, rgba(120,100,80,0.35) 0%, rgba(120,100,80,0) 100%),
      linear-gradient(90deg, rgba(255,255,255,0) 0%, rgba(255,255,255,0.25) 60%, rgba(255,255,255,0) 100%),
      linear-gradient(180deg, #e4e1dc 0%, #dcd6cc 28%, #cbbfae 48%, #a58f74 60%, #6f6558 72%, #3d3936 86%, #2e2c2b 100%);
  }
  .front-divider { position: absolute; left: 0; top: 0; }
  .banner { position: absolute; left: 0; color: var(--white); }
  .banner--headline { top: 49px; width: 236px; height: 86px; }
  .banner--address { top: 321px; width: 240px; height: 80px; }
  .banner svg { position: absolute; left: 0; top: 0; }
  .headline {
    position: absolute; left: 36px; top: 12px; font-weight: 400; font-size: 34px;
    letter-spacing: -0.5px; line-height: 1;
  }
  .headline-accent {
    position: absolute; left: 116px; top: 46px; font-weight: 500; font-size: 27px;
    color: var(--cyan); line-height: 1;
  }
  .address-title { position: absolute; left: 32px; top: 24px; font-size: 12.5px; white-space: nowrap; }
  .address-line { position: absolute; left: 32px; top: 42px; font-size: 12.5px; font-style: italic; white-space: nowrap; }

  .listing-photos { position: absolute; left: 352px; top: 0; width: 188px; height: 420px; }
  .listing { position: absolute; left: 0; width: 165px; text-align: center; }
  .listing-photo { display: block; width: 165px; height: 100px; }
  .listing-photo--bedroom { background: linear-gradient(170deg, #5fc3d2 0%, #bfe6ea 45%, #e9eee6 65%, #8fa55a 100%); }
  .listing-photo--living { background: linear-gradient(180deg, #d9a46c 0%, #e9c79b 38%, #a8825c 62%, #4e3a2a 100%); }
  .listing-photo--exterior { background: linear-gradient(180deg, #2f7fd3 0%, #8fc0ee 40%, #d8dde2 70%, #6c8a4e 100%); }
  .listing-caption { display: block; margin-top: 4px; font-size: 14px; line-height: 17px; color: var(--caption); }
  .listing-caption--strong { font-weight: 500; }

  /* Back */
  .back-fade {
    position: absolute; left: 369px; top: 0; width: 171px; height: 420px;
    background: linear-gradient(90deg, #ffffff 0%, #f2f2f2 55%, #d4d4d4 100%);
  }
  .info-panel {
    position: absolute; left: 21px; top: 14px; width: 348px; height: 398px;
    background: linear-gradient(160deg, var(--panel-top) 0%, var(--panel-mid) 55%, #2a2a2a 100%);
    color: var(--white);
  }
  .info-panel-sheen { position: absolute; left: 0; top: 0; }
  .panel-title { position: absolute; left: 0; width: 100%; top: 66px; text-align: center; font-weight: 700; font-size: 14px; }
  .panel-slogan { position: absolute; left: 0; width: 100%; top: 84px; text-align: center; font-size: 12px; color: var(--cyan); letter-spacing: 0.4px; }
  .service-list { position: absolute; left: 33px; top: 128px; list-style: none; }
  .service-list li { font-size: 12.5px; color: var(--lorem); line-height: 26px; }
  .contact-block {
    position: absolute; left: 0; top: 276px; width: 100%; height: 122px;
    background: var(--panel-black);
  }
  .contact-cta {
    position: absolute; left: 78px; top: 22px; font-family: "Roboto Condensed", Arial, sans-serif;
    font-weight: 700; font-size: 16px; color: var(--cyan); letter-spacing: -0.2px; white-space: nowrap;
  }
  .contact-cta svg { position: absolute; left: -26px; top: -2px; }
  .contact-phone { position: absolute; left: 110px; top: 42px; font-size: 16px; letter-spacing: 1px; }
  .contact-visit {
    position: absolute; left: 136px; top: 68px; font-family: "Roboto Condensed", Arial, sans-serif;
    font-weight: 700; font-size: 15px; color: var(--cyan);
  }
  .contact-url { position: absolute; left: 56px; top: 86px; font-size: 13px; letter-spacing: 0.5px; white-space: nowrap; }
  .contact-url-initial { font-weight: 700; font-size: 24px; color: var(--cyan); vertical-align: -3px; }
  .tree-emblem {
    position: absolute; left: 402px; top: 315px; width: 100px; height: 80px;
    border-radius: 50% 50% 46% 46%;
    background: radial-gradient(ellipse at 50% 45%, #2a2a2a 0%, var(--emblem) 70%);
  }
</style>
</head>
<body>

<section class="postcard postcard--front" aria-label="Postcard front">
  <div class="hero-photo" role="img" aria-label="Photo of a bright dining room with white shelving, wooden table and glossy dark floor"></div>

  <svg class="front-divider" width="540" height="420" viewBox="0 0 540 420" aria-hidden="true">
    <polygon points="321,0 540,0 540,420 321,420 347,210" fill="var(--column-bg)"/>
    <polyline points="316,0 342,210 316,420" fill="none" stroke="var(--cyan)" stroke-width="5"/>
  </svg>

  <div class="banner banner--headline">
    <svg width="236" height="86" viewBox="0 0 236 86" aria-hidden="true">
      <polygon points="0,0 206,0 236,43 206,86 0,86" fill="var(--band)"/>
    </svg>
    <span class="headline">Opportunity</span>
    <span class="headline-accent">Sale!</span>
  </div>

  <div class="banner banner--address">
    <svg width="240" height="80" viewBox="0 0 240 80" aria-hidden="true">
      <polygon points="0,0 210,0 240,40 210,80 0,80" fill="var(--band)"/>
    </svg>
    <span class="address-title">This Home For Sale By Owner!</span>
    <span class="address-line">123 Example Street, Indianapolis</span>
  </div>

  <div class="listing-photos">
    <figure class="listing" style="top:14px">
      <span class="listing-photo listing-photo--bedroom" role="img" aria-label="Photo of a renovated bedroom"></span>
      <figcaption class="listing-caption">Own It!</figcaption>
    </figure>
    <figure class="listing" style="top:150px">
      <span class="listing-photo listing-photo--living" role="img" aria-label="Photo of a living room at sunset"></span>
      <figcaption class="listing-caption listing-caption--strong">Restore it!</figcaption>
    </figure>
    <figure class="listing" style="top:286px">
      <span class="listing-photo listing-photo--exterior" role="img" aria-label="Photo of a house exterior under blue sky"></span>
      <figcaption class="listing-caption listing-caption--strong">Profit by it!</figcaption>
    </figure>
  </div>
</section>

<section class="postcard postcard--back" aria-label="Postcard back">
  <div class="back-fade"></div>
  <div class="info-panel">
    <svg class="info-panel-sheen" width="348" height="276" viewBox="0 0 348 276" aria-hidden="true">
      <polygon points="0,0 348,0 348,80 0,170" fill="rgba(255,255,255,0.06)"/>
    </svg>
    <p class="panel-title">Get more with Prime Door Homes.com!</p>
    <p class="panel-slogan">Any other slogan here.</p>
    <ul class="service-list">
      <li>Lorem ipsum dolor - sit amet si consectetur</li>
      <li>Lorem ipsum dolor - sit amet consectetur</li>
      <li>Lorem ipsum dolor - sit amet conse</li>
      <li>Lorem ipsum dolor - sit amet consectetur is</li>
      <li>Lorem ipsum dolor - sit amet consectetur</li>
    </ul>
    <div class="contact-block">
      <p class="contact-cta">
        <svg width="18" height="22" viewBox="0 0 18 22" aria-hidden="true">
          <path d="M4 1 L8 6 L6 9 C7 12 9 14 11 15 L13 13 L17 17 L14 21 C7 20 1 12 1 5 Z" fill="var(--cyan)"/>
        </svg>
        Call to GET MORE today!
      </p>
      <p class="contact-phone">317-555-0148</p>
      <p class="contact-visit">Or VISIT</p>
      <p class="contact-url"><span class="contact-url-initial">W</span>www.PrimeDoorHomes.com</p>
    </div>
  </div>
  <div class="tree-emblem" role="img" aria-label="Silhouette illustration of a tree"></div>
</section>

</body>
</html>
```